Belvoro Website

I need a website for a startup company that provides GIS (Geographic Information Services) staffing and products for local cities. Current website is www.belvorogroup.com

```html
<!DOCTYPE html>
<html lang="en">
<head>
<meta charset="UTF-8">
<title>Belvoro Group</title>
<link rel="stylesheet" href="https://fonts.googleapis.com/css2?family=Inter:wght@400;700;800&family=Poppins:wght@400;500;700&display=swap">
<style>
  :root {
    --ink: #111111;
    --white: #ffffff;
    --accent: #1e8fd3;
    --footer-bg: #202020;
    --footer-base: #1c1c1c;
    --hero-dark: #0e0a1c;
    --hero-teal: #2d6b72;
    --faint-line: #f1f1f1;
  }
  * { box-sizing: border-box; margin: 0; padding: 0; }
  html, body { width: 925px; height: 1200px; overflow: hidden; background: var(--white); }
  body { position: relative; font-family: "Inter", sans-serif; color: var(--ink); }

  .hero {
    position: absolute; left: 0; top: 0; width: 925px; height: 464px;
    background:
      radial-gradient(ellipse 260px 170px at 560px 200px, rgba(206,226,220,0.55), transparent 70%),
      radial-gradient(ellipse 300px 260px at 820px 300px, rgba(70,140,150,0.55), transparent 70%),
      linear-gradient(90deg, var(--hero-dark) 0%, #1a1526 35%, #233a48 62%, var(--hero-teal) 100%);
  }
  .brand {
    position: absolute; left: 77px; top: 31px;
    font-family: "Poppins", sans-serif; font-weight: 700; font-size: 20px; color: var(--white);
  }
  .main-nav { position: absolute; right: 78px; top: 34px; display: flex; gap: 14px; }
  .main-nav a {
    font-family: "Poppins", sans-serif; font-size: 10.5px; letter-spacing: 0.9px;
    color: var(--white); text-decoration: none;
  }
  .hero-eyebrow {
    position: absolute; left: 77px; top: 159px;
    font-weight: 700; font-size: 10.5px; color: var(--white);
  }
  .hero-title {
    position: absolute; left: 77px; top: 182px; width: 360px;
    font-weight: 800; font-size: 43px; line-height: 51px; letter-spacing: -1px; color: var(--white);
  }
  .button {
    position: absolute; display: flex; align-items: center; justify-content: center;
    background: var(--accent); color: var(--white); border-radius: 3px;
    font-size: 17px; font-weight: 400; text-decoration: none;
  }
  .hero-cta { left: 77px; top: 309px; width: 144px; height: 37px; }

  .about {
    position: absolute; left: 0; top: 464px; width: 925px; height: 450px;
    background: linear-gradient(180deg, #fbfbfb, var(--white));
  }
  .about-text {
    position: absolute; left: 77px; top: 113px; width: 305px;
    font-size: 17px; line-height: 27.4px;
  }
  .services-cta { left: 77px; top: 300px; width: 136px; height: 37px; }
  .about-photo {
    position: absolute; left: 541px; top: 89px; width: 306px; height: 270px; border-radius: 4px;
    background:
      radial-gradient(ellipse 70px 90px at 110px 170px, rgba(200,150,120,0.6), transparent 70%),
      linear-gradient(135deg, #e4e2d8, #d8d6cc 60%, #cfcab4);
  }
  .accent-square {
    position: absolute; left: 492px; top: 213px; width: 103px; height: 86px;
    background: var(--accent); border-radius: 3px;
  }

  .site-footer {
    position: absolute; left: 0; top: 914px; width: 925px; height: 286px; background: var(--footer-bg);
    font-family: "Poppins", sans-serif; color: var(--white);
  }
  .footer-brand {
    position: absolute; left: 77px; top: 69px;
    font-weight: 700; font-size: 18.5px; line-height: 18.5px;
  }
  .footer-col { position: absolute; top: 63px; }
  .footer-col h3 { font-weight: 400; font-size: 11px; margin-bottom: 17px; }
  .footer-col p, .footer-col a {
    display: block; font-size: 8.6px; line-height: 17.3px; color: var(--white); text-decoration: none;
  }
  .col-contact { left: 345px; }
  .col-menu { left: 550px; }
  .col-services { left: 724px; }
  .footer-base {
    position: absolute; left: 0; top: 225px; width: 925px; height: 61px; background: var(--footer-base);
  }
  .copyright { position: absolute; left: 77px; top: 26px; font-size: 7.8px; }
  .social-dot {
    position: absolute; left: 828px; top: 21px; width: 18px; height: 18px;
    border-radius: 50%; background: var(--white);
  }
</style>
</head>
<body>
  <header class="hero" role="img" aria-label="Photo of a hand touching a world map on a tablet screen">
    <div class="brand">Belvoro Group</div>
    <nav class="main-nav">
      <a href="#">SERVICES</a>
      <a href="#">CONTACT</a>
    </nav>
    <p class="hero-eyebrow">Belvoro Group</p>
    <h1 class="hero-title">We Make GIS Work For You</h1>
    <a class="button hero-cta" href="#">Call To Action</a>
  </header>

  <section class="about">
    <p class="about-text">We are an innovative team of geospatial experts with 25 years of experience in the field of GIS. We specialize in providing results-driven GIS solutions for local government and the private sector.</p>
    <a class="button services-cta" href="#">Our Services</a>
    <div class="about-photo" role="img" aria-label="Photo of a hand pointing at an antique world map"></div>
    <div class="accent-square"></div>
  </section>

  <footer class="site-footer">
    <div class="footer-brand">Belvoro<br>Group</div>
    <div class="footer-col col-contact">
      <h3>Contact</h3>
      <p>4180 W. Orchard Ave. #212</p>
      <p>Brookdale, CA 90417</p>
    </div>
    <div class="footer-col col-menu">
      <h3>Menu</h3>
      <a href="#">Home</a>
      <a href="#">Services</a>
      <a href="#">Contact Us</a>
    </div>
    <div class="footer-col col-services">
      <h3>Services</h3>
      <a href="#">GIS Consulting</a>
      <a href="#">GIS Applications</a>
      <a href="#">Spatial Data Solutions</a>
    </div>
    <div class="footer-base">
      <p class="copyright">© 2024 – belvorogroup</p>
      <span class="social-dot" aria-label="Social profile"></span>
    </div>
  </footer>
</body>
</html>
```